Mini Market Tolvo Business Presentation Cards

We need presentation cards with a logo we already own designed at this website as well. We need the printing, delivery and sleek, modem design in harmony with our previous logo design.

Target Market(s)

Low, med and High income class.

Industry/Entity Type

Grocery Store

Contact Information for Business Card

Business logo (Mini Market Tolvo), name: Esteban L. Morales/Lidia E. Paredes/ Iván Paredes (those are the names for the different cards),
Address: Col. Lomas del Valle, carretera a Tegel a 150mts del Centro Vial. Puerto Cortés, Honduras.
Email: minimarkettolvo@correofalso.hn
Teléfono: (504) 9715-3068

Font styles to use
Serif
Sans Serif

Requirements
Must have
• Business logo (Mini Market Tolvo), person name, department,
• Address, phone number, email address.

```html
<!DOCTYPE html>
<html lang="es">
<head>
<meta charset="utf-8">
<title>Mini Market Tolvo – Tarjeta de presentación</title>
<link href="https://fonts.googleapis.com/css2?family=Roboto:wght@400;700&family=Roboto+Condensed:wght@700&display=swap" rel="stylesheet">
<style>
  :root {
    --bg: #d9d6d1;
    --card: #ffffff;
    --brand-red: #e0412f;
    --brand-green: #86bd4c;
    --soft-grey: #e4e5e7;
    --text-grey: #55585c;
  }
  html, body {
    margin: 0;
    width: 1200px;
    height: 1200px;
    overflow: hidden;
    background: var(--bg);
  }
  .card {
    position: absolute;
    left: 60px;
    top: 285px;
    width: 1080px;
    height: 630px;
    background: var(--card);
    overflow: hidden;
    box-shadow: 0 6px 24px rgba(0,0,0,0.18);
  }
  .card__backdrop-circle {
    position: absolute;
    left: 632px;
    top: 0;
    width: 624px;
    height: 624px;
    border-radius: 50%;
    background: var(--soft-grey);
  }
  .brand {
    position: absolute;
    left: 82px;
    top: 108px;
    width: 320px;
    margin: 0;
    font-family: "Roboto", Arial, sans-serif;
    font-weight: 400;
    font-size: 56px;
    line-height: 62px;
    color: var(--brand-red);
  }
  .brand__dot {
    position: absolute;
    left: 412px;
    top: 68px;
    width: 228px;
    height: 228px;
    border-radius: 50%;
    background: var(--brand-green);
  }
  .person-name {
    position: absolute;
    left: 82px;
    top: 322px;
    margin: 0;
    font-family: "Roboto Condensed", "Arial Narrow", sans-serif;
    font-weight: 700;
    font-size: 33px;
    line-height: 40px;
    color: var(--brand-green);
    letter-spacing: 0.5px;
  }
  .department {
    position: absolute;
    left: 82px;
    top: 364px;
    margin: 0;
    font-family: "Roboto", Arial, sans-serif;
    font-size: 21px;
    line-height: 26px;
    color: var(--text-grey);
  }
  .contact {
    position: absolute;
    left: 82px;
    top: 412px;
    margin: 0;
    padding: 0;
    list-style: none;
    font-family: "Roboto", Arial, sans-serif;
    font-size: 26px;
    line-height: 33px;
    color: var(--text-grey);
  }
  .contact__item { position: relative; padding-left: 32px; }
  .contact__icon {
    position: absolute;
    left: 0;
    top: 7px;
    width: 20px;
    height: 20px;
    fill: var(--brand-green);
  }
  .contact__item--phone { color: var(--brand-red); font-weight: 700; }
</style>
</head>
<body>
  <div class="card">
    <div class="card__backdrop-circle"></div>

    <div class="brand__dot"></div>
    <p class="brand">Mini Market Tolvo</p>

    <h1 class="person-name">ESTEBAN L. MORALES</h1>
    <p class="department">Gerencia General</p>

    <ul class="contact">
      <li class="contact__item">
        <svg class="contact__icon" viewBox="0 0 20 20" aria-hidden="true"><path d="M10 1a7 7 0 0 0-7 7c0 5 7 11 7 11s7-6 7-11a7 7 0 0 0-7-7zm0 10a3 3 0 1 1 0-6 3 3 0 0 1 0 6z"/></svg>
        Col. Lomas del Valle,<br>
        Carretera a Tegel a 150mts del Centro Vial.<br>
        Puerto Cortés, Honduras.
      </li>
      <li class="contact__item">
        <svg class="contact__icon" viewBox="0 0 20 20" aria-hidden="true"><path d="M10 1a7 7 0 0 0-7 7c0 5 7 11 7 11s7-6 7-11a7 7 0 0 0-7-7zM6 6h8v5H6zm1 1l3 2 3-2z"/></svg>
        minimarkettolvo@correofalso.hn
      </li>
      <li class="contact__item contact__item--phone">
        <svg class="contact__icon" viewBox="0 0 20 20" aria-hidden="true"><path d="M10 1a7 7 0 0 0-7 7c0 5 7 11 7 11s7-6 7-11a7 7 0 0 0-7-7zM7.5 4.5l1.5 2-1 1c.5 1.2 1.3 2 2.5 2.5l1-1 2 1.5-1 1.5c-3 0-6-3-6-6z"/></svg>
        (504) 9715-3068
      </li>
    </ul>
  </div>
</body>
</html>
```